Flyer-Design für Ferienhaus auf Sylt
Zielgruppe
Ferienhaus auf Sylt im ruhigen und traditionellen Ort Archsum. Zielgruppe ruhe- und erholungssuchende Erwachsene, Familien mit Kind und evtl. mit Hund. Ferienhaus 'klein, aber fein' in ruhiger Lager mit großem Grundstück.
Homepage: duenenkate-wiesmoor.de
Aufgabenstellung
Format DIN LANG / 4 Seiten: Es sollen keine Saisonzeiten und auch keine Preise genannt werden. Es soll nur genannt werden, dass das Haus ab 50 EUR / Tag gemietet werden kann. Bitte nicht die vollständige Adresse des Objektes angeben, lediglich „Sylt-Archsum“. Kontakdtaen bitte auf der Rückseite nennen (siehe Homepage). Kontaktaufnahme bevorzugt per Mail / Anfrageformular v. Homepage. Gerne meine Bilder nutzen, bin aber auch offen für 2-3 Bilder aus dem Stock. Kleine Texte formulieren und gerne mehrere Bilder des Hauses zeigen.

```html
<!DOCTYPE html>
<html lang="de">
<head>
<meta charset="utf-8">
<title>Dünenkate Wiesmoor – Flyer</title>
<link rel="stylesheet" href="https://fonts.googleapis.com/css2?family=Libre+Bodoni&family=Mulish:wght@400&family=Parisienne&display=swap">
<style>
:root{
  --stage:#c6c6c6;
  --paper:#ffffff;
  --band:#4a7ba6;
  --mark:#2f6e9c;
  --ink:#1f2328;
  --accent:#3b74a3;
}
*{margin:0;padding:0;box-sizing:border-box}
html,body{width:667px;height:1200px;overflow:hidden;background:var(--stage)}
body{position:relative;font-family:"Mulish",sans-serif;color:var(--ink)}
.spread{position:absolute;left:71px;width:532px;height:532px;background:var(--paper);box-shadow:0 1px 3px rgba(0,0,0,.25)}
.spread--outer{top:45px}
.spread--inner{top:623px}
.abs{position:absolute}
.photo{position:absolute}
.serif{font-family:"Libre Bodoni",serif;white-space:nowrap}
.script{font-family:"Parisienne",cursive;white-space:nowrap}
.band{position:absolute;background:var(--band);color:#fff;text-align:center}
.dot{position:absolute;border-radius:50%}
.contact-label{left:30px;top:207px;font-size:10px;line-height:12px;color:var(--accent);letter-spacing:.2px}
.contact-rule{left:100px;top:207px;width:1px;height:87px;background:var(--band)}
.contact-list{left:106px;top:208px;font-size:10px;line-height:13.5px}
.contact-list p{white-space:nowrap}
.intro{left:297px;width:206px;font-size:8px;line-height:10.4px;text-align:justify}
.features{left:0;top:388px;width:266px;text-align:center;font-size:8.2px;line-height:14.3px}
.features p{white-space:nowrap}
</style>
</head>
<body>

<section class="spread spread--outer">
  <!-- Rückseite -->
  <div class="photo" style="left:0;top:0;width:266px;height:122px;background:linear-gradient(#bfe3ef 0%,#d8edf2 35%,#7fa35a 60%,#4f7d33 100%)" role="img" aria-label="Foto: Ferienhaus mit spitzem Dach hinter Hecken und Wiese"></div>
  <div class="band" style="left:0;top:122px;width:266px;height:66px"></div>
  <div class="dot" style="left:118px;top:104px;width:30px;height:30px;background:#fff"></div>
  <div class="abs serif" style="left:0;top:136px;width:266px;text-align:center;color:#fff;font-size:18px">Dünenkate Wiesmoor</div>
  <div class="abs" style="left:0;top:162px;width:266px;text-align:center;color:#fff;font-size:9.5px">Sylt-Archsum</div>

  <div class="abs contact-label">ANFRAGEN &amp;<br>BUCHUNGEN</div>
  <div class="abs contact-rule"></div>
  <div class="abs contact-list">
    <p>T: 030 555 014 27</p>
    <p>M: 0172 55 901 64</p>
    <p>F: 030 555 018 93</p>
    <p style="margin-top:8px">strandkatehuus@post.de</p>
    <p style="margin-top:8px">duenenkate-wiesmoor.de</p>
  </div>

  <div class="photo" style="left:0;top:312px;width:131px;height:110px;background:linear-gradient(#6f7c92 0%,#e9a064 35%,#7a5a3a 65%,#5b4a2b 100%)" role="img" aria-label="Foto: Sonnenuntergang über Landstraße"></div>
  <div class="photo" style="left:133px;top:312px;width:133px;height:110px;background:linear-gradient(#6d86b8 0%,#b9c9de 35%,#9ea36a 60%,#c8a27a 100%)" role="img" aria-label="Foto: Holzsteg durch die Dünen zum Meer"></div>
  <div class="photo" style="left:0;top:424px;width:131px;height:108px;background:linear-gradient(#9fc9e6 0%,#d9e6ee 35%,#e8e2d6 60%,#a6a566 100%)" role="img" aria-label="Foto: Strand mit Bank zwischen Dünengras"></div>
  <div class="photo" style="left:133px;top:424px;width:133px;height:108px;background:linear-gradient(#c3cedb 0%,#8c9aa6 30%,#6b5a4b 60%,#9a5b3c 100%)" role="img" aria-label="Foto: Strandkörbe am Kliff"></div>
  <div class="dot" style="left:78px;top:368px;width:108px;height:108px;background:#fff"></div>
  <div class="dot" style="left:81px;top:371px;width:102px;height:102px;background:linear-gradient(#9ccbe0 0%,#b6d9e6 35%,#a35a48 55%,#6e9a45 80%)" role="img" aria-label="Foto: Ferienhaus aus rotem Backstein mit runden Fenstern"></div>

  <!-- Titelseite -->
  <div class="photo" style="left:266px;top:0;width:266px;height:272px;background:linear-gradient(#8fc5dc 0%,#bfe0ea 30%,#3a3f45 45%,#a1523f 62%,#6e9a45 80%,#5b8a38 100%)" role="img" aria-label="Foto: Backsteinhaus mit spitzem Dach auf grüner Wiese"></div>
  <div class="dot" style="left:372px;top:216px;width:64px;height:64px;background:#fff"></div>
  <div class="band" style="left:266px;top:273px;width:266px;height:45px"></div>
  <div class="abs serif" style="left:266px;top:282px;width:266px;text-align:center;color:#fff;font-size:23px;line-height:28px">Dünenkate Wiesmoor</div>
  <div class="abs" style="left:266px;top:318px;width:266px;height:1px;background:#fff"></div>
  <div class="photo" style="left:266px;top:319px;width:266px;height:213px;background:linear-gradient(#7fc1d8 0%,#b4dbe6 40%,#c9c78e 62%,#b2a662 80%,#8e8a48 100%)" role="img" aria-label="Foto: Leuchtturm hinter Dünengras"></div>
  <div class="abs script" style="left:266px;top:343px;width:266px;text-align:center;color:#fff;font-size:24px;line-height:26px">Ankommen und<br>wohlfühlen</div>
</section>

<section class="spread spread--inner">
  <div class="photo" style="left:0;top:0;width:266px;height:123px;background:linear-gradient(#9fcfe6 0%,#cfe6ee 35%,#7c9a55 60%,#5d8a36 100%)" role="img" aria-label="Foto: Haus mit Garten und Obstbäumen"></div>
  <div class="photo" style="left:0;top:127px;width:147px;height:106px;background:linear-gradient(#a7d0e6 0%,#5a4c44 30%,#a55440 55%,#dcdcdc 80%,#6e9a45 100%)" role="img" aria-label="Foto: Süd-Terrasse mit Gartenmöbeln und Strandkorb"></div>
  <div class="photo" style="left:150px;top:127px;width:116px;height:106px;background:linear-gradient(#9fcfe6 0%,#6e9a45 40%,#d68fa8 60%,#c9a879 100%)" role="img" aria-label="Foto: Sektflasche, Gläser und Blumen im Garten"></div>
  <div class="photo" style="left:0;top:236px;width:128px;height:105px;background:linear-gradient(#eae3cf 0%,#efe9da 50%,#d9d5cc 100%)" role="img" aria-label="Foto: Einbauküche"></div>
  <div class="photo" style="left:130px;top:236px;width:136px;height:105px;background:linear-gradient(#eef0f0 0%,#dcdcd6 45%,#b98a55 75%,#9c6c3c 100%)" role="img" aria-label="Foto: Essbereich mit Holztisch"></div>
  <div class="abs script" style="left:0;top:350px;width:266px;text-align:center;color:var(--accent);font-size:19px;line-height:26px">Ankommen und wohlfühlen</div>
  <div class="abs features">
    <p>Lichtdurchflutetes Wohnzimmer mit ausziehbarer Couch</p>
    <p>Moderne offene Einbauküche</p>
    <p>Badezimmer im Ober- und Erdgeschoss</p>
    <p>Schlafzimmer mit Doppelbett</p>
    <p>Zweites Schlafzimmer/Kinderzimmer</p>
    <p>PKW-Stellplatz</p>
    <p>Kostenfreies WLAN</p>
    <p>Kontaktlose Anreise mit persönlichem Pin-Code</p>
  </div>

  <div class="dot" style="left:381px;top:20px;width:42px;height:42px;background:var(--mark)"></div>
  <div class="abs serif" style="left:266px;top:61px;width:266px;text-align:center;color:var(--accent);font-size:19px">Dünenkate Wiesmoor</div>
  <p class="abs intro" style="top:108px">Kleines aber feines Ferienhaus im beschaulichen Ort Archsum auf Sylt in ruhiger Lage mit großem Garten.</p>
  <p class="abs intro" style="top:148px">Das freistehende, massiv gebaute Einfamilienhaus bietet Ruhe- und Erholungssuchenden mit ca. 86 m² Wohnfläche, der schönen Süd-Terrasse und dem großen Grundstück (1200 m²) die besten Voraussetzungen zum Entspannen, Sonne tanken und um sich einfach nur wohlzufühlen.</p>
  <p class="abs intro" style="top:219px;text-align:left">Ideal für 2-6 Personen<br>Verfügbar bereits ab € 50,- Tagesmiete</p>

  <div class="photo" style="left:266px;top:268px;width:153px;height:109px;background:linear-gradient(#e4e6ec 0%,#d6d9e2 40%,#3f4f9a 65%,#b88a55 100%)" role="img" aria-label="Foto: Wohnzimmer mit blauer Ecksofa-Couch"></div>
  <div class="photo" style="left:422px;top:268px;width:110px;height:109px;background:linear-gradient(#b9c9da 0%,#e6ebee 35%,#9aa9b5 60%,#3e4a52 100%)" role="img" aria-label="Foto: Abendsonne über dem Meer"></div>
  <div class="photo" style="left:266px;top:380px;width:128px;height:105px;background:linear-gradient(#eceae4 0%,#d9d2c4 50%,#3f4248 80%,#5b5f63 100%)" role="img" aria-label="Foto: Badezimmer mit Waschtisch"></div>
  <div class="photo" style="left:397px;top:380px;width:135px;height:105px;background:linear-gradient(#f1f0ec 0%,#e5e0d6 35%,#5a6aa0 55%,#c09458 80%,#d9b98a 100%)" role="img" aria-label="Foto: Schlafzimmer mit Doppelbett"></div>
  <div class="band" style="left:266px;top:488px;width:266px;height:44px"></div>
  <div class="abs" style="left:266px;top:497px;width:266px;text-align:center;color:#fff;font-size:8px">Alle Details und Buchungsmöglichkeit auf</div>
  <div class="abs serif" style="left:266px;top:507px;width:266px;text-align:center;color:#fff;font-size:12px">duenenkate-wiesmoor.de</div>
</section>

</body>
</html>
```